Billboard for personal injury chiropractors office

We are a personal injury chiropractor clinic.
I need a Billboard with the company name as the dominating factor. Also a smaller picture or 2 of something creative, like a car accident or an arm in a cast off to the sides.
We Like something Clean and Simple and Eye Catching. Please make the picture Small and Off To The Side. The MAIN FOCUS areas are the… name Varden Chiropractic Clinic
At the top CAR ACCIDENT INJURY?
AND at the bottom our number 418-27-FLEXA.
Dr.Milo R. Varden in bold somewhere with the word chiropractor under the doctors name in a text.

Im open to red lettering on white backgrounds, red on yellow backgrounds and I'm also open to reds blues white and yellow. I'd prefer yellow if used be across the bottom.

I am uploading a very rough draft of what we are after along with a screenshot of the tv commercial showing the yellow

DO NOT USE THE LOGO ON THE COMMERCIAL. I JUST WANT THE NAME TYPED LIKE ON SAMPLE BILLBOARD.

Industry/Entity Type

Chiropractic

Colors
0054AA
0677BA
7BADD7
CADEEF
E8F1F8
FFF300
FFF600
FEFA6F
FFFEC7
FFFEE8
EB3D1F
EC4F4E
F09395
F8D3D4
FCEDEE

Requirements
Must have
• Eye catching ,bold

```html
<!DOCTYPE html>
<html lang="en">
<head>
<meta charset="utf-8">
<title>Varden Chiropractic Clinic Billboard</title>
<link rel="stylesheet" href="https://fonts.googleapis.com/css2?family=Bebas+Neue&family=Montserrat:wght@400;600;700&display=swap">
<style>
  :root {
    --red: #d40000;
    --ink: #0d0d0d;
    --white: #ffffff;
    --backdrop: #a6a6a6;
    --road-light: #e6e7ec;
    --road-mid: #b9bbc4;
    --car-dark: #2b2e33;
  }
  * { margin: 0; padding: 0; box-sizing: border-box; }
  html, body {
    width: 1200px; height: 1200px; overflow: hidden;
    background: var(--backdrop);
  }
  .stage {
    width: 1200px; height: 1200px;
    display: flex; align-items: center; justify-content: center;
  }
  .billboard {
    position: relative;
    width: 1100px; height: 320px;
    background: var(--white);
    box-shadow: 0 8px 14px rgba(0,0,0,0.35);
    overflow: hidden;
  }
  .road-fade {
    position: absolute; left: 560px; right: 0; top: 210px; bottom: 0;
    background: linear-gradient(90deg, rgba(255,255,255,0) 0%, var(--road-light) 35%, var(--road-mid) 100%);
  }
  .road-line {
    position: absolute; left: 600px; right: 0; top: 214px; height: 4px;
    background: linear-gradient(90deg, rgba(255,255,255,0), var(--white));
  }
  .crash-photo {
    position: absolute; right: 0; top: 0; width: 380px; height: 320px;
    background: radial-gradient(ellipse at 60% 55%, var(--car-dark) 0%, #4a4d55 45%, rgba(120,122,130,0.6) 70%, rgba(255,255,255,0) 90%);
  }
  .clinic-name {
    position: absolute; left: 32px; top: 28px;
    font-family: "Bebas Neue", "Oswald", sans-serif;
    font-size: 84px; line-height: 1; letter-spacing: 0.5px;
    color: var(--red);
  }
  .headline {
    position: absolute; left: 32px; top: 110px;
    font-family: "Montserrat", sans-serif; font-weight: 600;
    font-size: 44px; line-height: 52px; letter-spacing: 1.5px;
    color: var(--ink); text-transform: uppercase;
  }
  .phone-band {
    position: absolute; left: 0; top: 240px;
    width: 445px; height: 58px;
    background: var(--red);
    border-radius: 0 29px 29px 0;
    display: flex; align-items: center; padding-left: 32px;
    font-family: "Montserrat", sans-serif; font-weight: 700;
    font-size: 46px; letter-spacing: 1px; color: var(--white);
  }
  .doctor {
    position: absolute; left: 463px; top: 246px;
    font-family: "Montserrat", sans-serif;
    font-size: 23px; line-height: 30px; letter-spacing: 0.8px;
  }
  .doctor-first { color: var(--red); font-weight: 700; }
  .doctor-last { color: var(--ink); font-weight: 700; }
  .doctor-title { color: var(--ink); font-weight: 400; }
</style>
</head>
<body>
<div class="stage">
  <section class="billboard">
    <div class="road-fade"></div>
    <div class="road-line"></div>
    <div class="crash-photo" role="img" aria-label="Photo of a dark car with a crushed front end on a road"></div>
    <h1 class="clinic-name">Varden Chiropractic Clinic</h1>
    <p class="headline">At the top<br>Car accident injury?</p>
    <div class="phone-band">418-27-FLEXA</div>
    <div class="doctor">
      <div class="doctor-first">DR.MILO R.</div>
      <div><span class="doctor-last">VARDEN</span> <span class="doctor-title">Chiropractor</span></div>
    </div>
  </section>
</div>
</body>
</html>
```